Design an awesome Website mock-up for FurHaven

Good day Freelancers,

This is a pretty simple website but it must look great.
The details are in the document provided, if you have any questions please ask :)

Required: Website mock-up

Design must be professional, sleek, and modern.

Try to use colors that express safety, compassion, and positive vibes.

I will make another contest for the Logo Design.

```html
<!DOCTYPE html>
<html lang="en">
<head>
<meta charset="utf-8">
<title>FurHaven</title>
<link href="https://fonts.googleapis.com/css2?family=Open+Sans:wght@300;400;600;700&display=swap" rel="stylesheet">
<style>
:root{
  --navy:#2f3791;
  --band:#3d4699;
  --btn:#2d3590;
  --green:#8db14b;
  --green-dark:#6f9536;
  --logo-bg:#dfe6c6;
  --nav-text:#4d6a6a;
  --ink:#333;
  --muted:#9a9a9a;
  --rule:#e6e6e6;
  --footer:#3b3b3b;
  --accent:#e0542a;
  --stat:#3c4c8f;
}
*{margin:0;padding:0;box-sizing:border-box}
html,body{width:1200px;height:2587px;overflow:hidden;background:#fff;font-family:"Open Sans",Arial,sans-serif;color:var(--ink)}
.page{position:relative;width:1200px;height:2587px}
.abs{position:absolute}
.topbar{left:0;top:0;width:1200px;height:37px;background:var(--navy)}
.account{right:140px;top:7px;color:#fff;font-size:17px;font-weight:600;letter-spacing:.2px}
.account .sep{margin:0 8px}
.account .donate{color:var(--accent)}
.navbar{left:0;top:37px;width:1200px;height:55px;background:#fff}
.brand{left:149px;top:0;width:239px;height:156px;background:var(--logo-bg);box-shadow:0 2px 4px rgba(0,0,0,.3);z-index:5;display:flex;align-items:center;justify-content:center;gap:10px}
.brand .dot{width:18px;height:18px;border-radius:50%;background:var(--accent)}
.brand span{font-size:30px;font-weight:700;color:var(--navy)}
.menu{left:404px;top:54px;display:flex;gap:18px;font-size:17px;color:var(--nav-text);font-weight:600}
.hero{left:0;top:92px;width:1200px;height:431px;background:linear-gradient(90deg,var(--green) 0%,#95b753 45%,var(--green-dark) 100%)}
.hero-photo{left:613px;top:92px;width:587px;height:431px;background:linear-gradient(90deg,#93b355 0%,#b99a5e 30%,#c9a06a 60%,#c24a3a 100%)}
.hero-title{left:0;top:222px;width:632px;text-align:center;color:#fff;font-size:40px;line-height:48px;font-weight:400}
.hero-sub{left:0;top:342px;width:632px;text-align:center;color:#fff;font-size:23px}
.btn{background:var(--btn);color:#fff;border-radius:4px;box-shadow:0 2px 3px rgba(0,0,0,.35);display:flex;align-items:center;justify-content:center;font-size:20px;font-weight:600}
.hero-btn{left:197px;top:397px;width:224px;height:40px}
.arrow{width:38px;height:38px;top:457px}
.grey-band{left:0;top:523px;width:1200px;height:26px;background:#d9d9d9}
h2{font-weight:400;font-size:21px;color:#222}
.projects-h{left:185px;top:586px}
.projects-desc{left:185px;top:625px;width:830px;font-size:16px;line-height:18px;color:#444}
.pet{width:173px}
.pet .img{width:173px;height:173px;border:1px solid #ccc}
.pet h3{margin-top:13px;font-size:19px;font-weight:400;line-height:22px}
.pet p{font-size:12px;line-height:16px;text-transform:uppercase;width:130px;color:#444}
.pager{left:893px;top:962px;display:flex;gap:7px;font-size:12px}
.pager span{width:18px;height:18px;display:flex;align-items:center;justify-content:center;background:#d6d6d6;color:#fff}
.pager span.on{background:none;color:#888}
.hr{height:1px;background:var(--rule)}
.sec-h{font-size:20px}
.welcome-h{left:200px;top:1068px;font-weight:600;color:#222}
.welcome-text{left:200px;top:1135px;width:390px;font-size:16.5px;line-height:20px;color:#333}
.welcome-text p+p{margin-top:20px}
.donate-btn{left:373px;top:1328px;width:192px;height:40px}
.help-item{left:621px;width:420px;display:flex;gap:11px}
.help-item .img{width:110px;height:72px;flex:none}
.help-item h4{font-size:17px;font-weight:400;line-height:19px;margin-top:6px}
.help-item p{font-size:12.5px;line-height:16px;color:var(--muted)}
.how{left:0;top:1441px;width:1200px;height:322px;background:var(--band);box-shadow:0 4px 6px rgba(0,0,0,.25)}
.how-h{left:185px;top:1486px;color:#fff;font-weight:600;font-size:20px}
.step{top:1538px;width:130px;text-align:center;color:#fff;font-size:14.5px;line-height:17px}
.step .c{width:100px;height:100px;border-radius:50%;background:#fff;margin:0 auto 22px;display:flex;align-items:center;justify-content:center}
.news-item{left:192px;display:flex;gap:13px;width:400px}
.news-item .img{width:117px;height:72px;flex:none}
.news-item h4{font-size:17px;font-weight:400;line-height:19px}
.news-item p{font-size:12.5px;line-height:16px;color:var(--muted)}
.partner{top:1883px;width:87px;font-size:12.5px;line-height:16px}
.partner .img{width:87px;height:65px;border:1px solid #ccc}
.partner h5{font-weight:400;margin-top:11px;height:34px;color:#333;font-size:12.5px}
.partner p{color:var(--muted);margin-top:11px;height:110px}
.partner small{font-size:11px;color:var(--muted)}
.totop{left:1135px;top:2149px;width:48px;height:47px;background:#9a9a9a;color:#fff;font-size:14px;font-weight:700;display:flex;flex-direction:column;align-items:center;justify-content:center;box-shadow:0 2px 3px rgba(0,0,0,.3)}
.footer{left:0;top:2224px;width:1200px;height:332px;background:var(--footer)}
.fcol{top:2274px;color:#fff;font-size:15px;line-height:18px}
.fcol b{font-weight:700;display:block}
.fcol .maps{font-style:italic;font-size:13px;margin-top:16px;color:#ddd}
.socials{left:819px;top:2457px;display:flex;gap:11px}
.socials span{width:30px;height:30px;display:block}
.bottom{left:0;top:2556px;width:1200px;height:31px;font-size:14.5px;color:var(--stat)}
.bottom .stats{left:105px;top:6px;display:flex;gap:42px}
.bottom .copy{right:96px;top:6px}
</style>
</head>
<body>
<div class="page">
  <div class="abs topbar"></div>
  <div class="abs account">SIGN UP<span class="sep">|</span>LOG IN<span class="sep">|</span><span class="donate">DONATE</span></div>
  <div class="abs navbar"></div>
  <div class="abs brand"><div class="dot"></div><span>FurHaven</span></div>
  <nav class="abs menu"><span>HOME</span><span>SAVED LIST</span><span>HOW WE WORK</span><span>HELP &amp; SUPPORT</span><span>CONTACT US</span>
    <svg width="18" height="18" viewBox="0 0 18 18" style="margin-top:3px"><circle cx="7" cy="7" r="5" fill="none" stroke="#aaa" stroke-width="2"/><line x1="11" y1="11" x2="16" y2="16" stroke="#aaa" stroke-width="2.5"/></svg>
  </nav>

  <section>
    <div class="abs hero"></div>
    <div class="abs hero-photo" role="img" aria-label="Golden retriever hugged by a young boy in a red shirt"></div>
    <h1 class="abs hero-title">THIS DOG JUST FOUND<br>A NEW HOME</h1>
    <p class="abs hero-sub">Be a part of our mission to help pets in need.</p>
    <div class="abs btn hero-btn">Get Involved</div>
    <svg class="abs arrow" style="left:32px" viewBox="0 0 38 38"><circle cx="19" cy="19" r="17" fill="var(--navy)" stroke="#fff" stroke-width="2"/><polyline points="22,12 15,19 22,26" fill="none" stroke="#fff" stroke-width="3"/></svg>
    <svg class="abs arrow" style="left:85px" viewBox="0 0 38 38"><circle cx="19" cy="19" r="17" fill="var(--navy)" stroke="#fff" stroke-width="2"/><polyline points="16,12 23,19 16,26" fill="none" stroke="#fff" stroke-width="3"/></svg>
    <div class="abs grey-band"></div>
  </section>

  <section>
    <h2 class="abs projects-h">Projects</h2>
    <p class="abs projects-desc">Lorem ipsum dolor sit amet, consectetuer adipiscing elit, sed diam nonummy nibh euismod tincidunt ut laoreet dolore magna aliquam erat volutpat.</p>
    <div class="abs pet" style="left:185px;top:684px"><div class="img" role="img" aria-label="Tan dog with a red collar" style="background:linear-gradient(135deg,#a06a3c,#6b4a2e)"></div><h3>TAKOTA</h3><p>Needs surgery to walk and play again</p></div>
    <div class="abs pet" style="left:407px;top:684px"><div class="img" role="img" aria-label="Bulldog face close-up" style="background:linear-gradient(135deg,#c9a88a,#8a6a55)"></div><h3>BEAN</h3><p>Needs surgery for his torn miniscus</p></div>
    <div class="abs pet" style="left:628px;top:684px"><div class="img" role="img" aria-label="Ginger cat" style="background:linear-gradient(135deg,#c98a6a,#a86a58)"></div><h3>KITTY</h3><p>Needs surgery to walk and play again</p></div>
    <div class="abs pet" style="left:849px;top:684px"><div class="img" role="img" aria-label="Black and white collie" style="background:linear-gradient(135deg,#3a4a5a,#8a6a4a)"></div><h3>DANA</h3><p>Needs surgery to walk and play again</p></div>
    <div class="abs pager"><span class="on">1</span><span>2</span><span>3</span><span>4</span><span>5</span></div>
    <div class="abs hr" style="left:185px;top:1009px;width:835px"></div>
  </section>

  <section>
    <h2 class="abs sec-h welcome-h">Welcome to FurHaven</h2>
    <div class="abs hr" style="left:200px;top:1105px;width:385px"></div>
    <div class="abs welcome-text"><p>Vivamus ut molestie nulla. Aenean vel tortor velit. Morbi quis varius tortor. Quisque sit amet leo purus, eget accumsan lorem.</p><p>Ut wisi enim ad minim veniam, quis nostrud exerci tation ullamcorper suscipit lobortis nisl ut aliquip ex ea commodo consequat. Duis autem vel eum iriure dolor.</p></div>
    <div class="abs btn donate-btn">Donate</div>

    <h2 class="abs sec-h" style="left:620px;top:1068px">Ways to Help</h2>
    <div class="abs hr" style="left:620px;top:1105px;width:385px"></div>
    <div class="abs help-item" style="top:1121px"><div class="img" role="img" aria-label="Volunteer holding a rescued kitten" style="background:linear-gradient(135deg,#d06a3a,#8a5a4a)"></div><div><h4>Rescue Pets</h4><p>Lorem ipsum dolor sit amet, consectetuer adipiscing elit<br>Read more +</p></div></div>
    <div class="abs help-item" style="top:1211px"><div class="img" role="img" aria-label="Woman with an adopted puppy" style="background:linear-gradient(135deg,#4a3a3a,#b0a0a0)"></div><div><h4>Adopt Pets</h4><p>Lorem ipsum dolor sit amet, consectetuer adipiscing elit<br>Read more +</p></div></div>
    <div class="abs help-item" style="top:1300px"><div class="img" role="img" aria-label="Family with pets at a shelter" style="background:linear-gradient(135deg,#a89070,#6a7a6a)"></div><div><h4>Donate to FurHaven</h4><p>Lorem ipsum dolor sit amet, consectetuer adipiscing elit<br>Read more +</p></div></div>
  </section>

  <section>
    <div class="abs how"></div>
    <h2 class="abs how-h">This is how FurHaven works</h2>
    <div class="abs step" style="left:171px"><div class="c"><svg width="54" height="54" viewBox="0 0 54 54" fill="var(--band)"><rect x="14" y="6" width="30" height="38"/><rect x="8" y="12" width="30" height="38" fill="#fff" stroke="var(--band)" stroke-width="3"/><rect x="14" y="20" width="18" height="3"/><rect x="14" y="27" width="18" height="3"/><rect x="14" y="34" width="18" height="3"/></svg></div>1. Sign Up a<br>Project</div>
    <div class="abs step" style="left:295px"><div class="c"><svg width="54" height="54" viewBox="0 0 54 54"><polyline points="8,28 22,42 48,10" fill="none" stroke="var(--band)" stroke-width="8"/></svg></div>2. Project is<br>Evaluated</div>
    <div class="abs step" style="left:418px"><div class="c"><svg width="56" height="56" viewBox="0 0 56 56"><circle cx="28" cy="28" r="25" fill="var(--band)"/><text x="28" y="39" text-anchor="middle" font-size="32" font-weight="700" fill="#fff" font-family="Open Sans, sans-serif">$</text></svg></div>3. People Starts<br>Donating</div>
    <div class="abs step" style="left:542px"><div class="c"><svg width="60" height="54" viewBox="0 0 60 54"><rect x="4" y="4" width="52" height="36" fill="none" stroke="var(--band)" stroke-width="4"/><polyline points="12,32 24,22 32,28 46,12" fill="none" stroke="var(--band)" stroke-width="4"/><rect x="24" y="40" width="12" height="6" fill="var(--band)"/><rect x="16" y="46" width="28" height="4" fill="var(--band)"/></svg></div>4. Project is<br>Ended</div>
    <div class="abs step" style="left:666px"><div class="c"><svg width="50" height="54" viewBox="0 0 50 54" fill="var(--band)"><rect x="10" y="8" width="6" height="26" rx="3"/><rect x="18" y="3" width="6" height="30" rx="3"/><rect x="26" y="4" width="6" height="30" rx="3"/><rect x="34" y="9" width="6" height="26" rx="3"/><path d="M10 28 H40 V40 Q40 50 28 50 H22 Q12 50 8 40 L2 28 Q6 24 10 30Z"/></svg></div>5. Money is<br>Collected</div>
    <div class="abs step" style="left:790px"><div class="c"><svg width="54" height="54" viewBox="0 0 54 54"><path d="M6 28 L12 10 H42 L48 28 V46 H6Z" fill="var(--band)"/><rect x="12" y="28" width="30" height="10" fill="#fff"/><polyline points="20,22 27,14 34,22" fill="none" stroke="#fff" stroke-width="4"/><line x1="27" y1="15" x2="27" y2="30" stroke="#fff" stroke-width="4"/></svg></div>6. Project is<br>Paid Directly</div>
    <div class="abs step" style="left:907px"><div class="c"><svg width="56" height="54" viewBox="0 0 56 54" fill="var(--band)"><rect x="4" y="6" width="36" height="26" rx="3"/><path d="M16 18 H52 V42 H30 L20 50 V42 H16Z" stroke="#fff" stroke-width="3"/></svg></div>7. Funders are<br>Notified</div>
  </section>

  <section>
    <h2 class="abs sec-h" style="left:192px;top:1832px">FurHaven News</h2>
    <div class="abs hr" style="left:192px;top:1870px;width:390px"></div>
    <div class="abs news-item" style="top:1887px"><div class="img" role="img" aria-label="Family posing with their new dog" style="background:linear-gradient(135deg,#6a5a4a,#b08a6a)"></div><div><h4>New Family for Ivan</h4><p>Lorem ipsum dolor sit amet, consectetuer adipiscing elit<br>Read more +</p></div></div>
    <div class="abs news-item" style="top:1975px"><div class="img" role="img" aria-label="Happy brindle dog" style="background:linear-gradient(135deg,#5a4a3a,#9a8a7a)"></div><div><h4>New Shelter provided</h4><p>Lorem ipsum dolor sit amet, consectetuer adipiscing elit</p></div></div>
    <div class="abs news-item" style="top:2065px"><div class="img" role="img" aria-label="Black and white cat" style="background:linear-gradient(135deg,#2a2a3a,#6a6a7a)"></div><div><h4>Kitty Saved Yesterday</h4><p>Lorem ipsum dolor sit amet, consectetuer adipiscing elit</p></div></div>

    <h2 class="abs sec-h" style="left:624px;top:1832px">Our Partners</h2>
    <div class="abs hr" style="left:624px;top:1870px;width:385px"></div>
    <div class="abs partner" style="left:621px"><div class="img" role="img" aria-label="Panda" style="background:linear-gradient(135deg,#e8e8e8,#7a7a7a)"></div><h5>Adopt a Pet Program</h5><p>Lorem ipsum dolor sit amet, con-sectetuer adipiscing elit, sed diam</p><small>Support +</small></div>
    <div class="abs partner" style="left:721px"><div class="img" role="img" aria-label="Tiger" style="background:linear-gradient(135deg,#c8843a,#5a4a2a)"></div><h5>Pet Lovers Association</h5><p>Lorem ipsum dolor sit amet, con-sectetuer adipiscing elit, sed diam</p><small>Support +</small></div>
    <div class="abs partner" style="left:821px"><div class="img" role="img" aria-label="Penguin on snow" style="background:linear-gradient(180deg,#3a5aa8,#e8eef8)"></div><h5>Help Shel-ters Program</h5><p>Lorem ipsum dolor sit amet, con-sectetuer adipiscing elit, sed</p><small>Support +</small></div>
    <div class="abs partner" style="left:923px"><div class="img" role="img" aria-label="Grey kitten" style="background:linear-gradient(135deg,#8a8a7a,#4a4a3a)"></div><h5>Against Cruelty</h5><p>Lorem ipsum dolor sit amet, con-sectetuer adipiscing elit, sed</p><small>Support +</small></div>

    <div class="abs totop"><svg width="16" height="9" viewBox="0 0 16 9"><polyline points="1,8 8,1 15,8" fill="none" stroke="#fff" stroke-width="2"/></svg>TOP</div>
  </section>

  <footer>
    <div class="abs footer"></div>
    <div class="abs fcol" style="left:191px"><b>PRESS</b>Recent Posts<br>News &amp; Events<br>Updates<br>Media<br>Community</div>
    <div class="abs fcol" style="left:401px"><b>PAGES</b>About<br>Projects<br>Saved List<br>How We Work<br>Privacy<br>Terms<br>Feedback</div>
    <div class="abs fcol" style="left:608px"><b>QUICK LINKS</b>Sign Up<br>Donate<br>Help &amp; Support<br>Contact Us</div>
    <div class="abs fcol" style="left:819px"><b>GET IN TOUCH</b>T: (312) 555 01 47<br>E: hello@furhaven.org<br><br><b>FURHAVEN</b>48 Maple Row, 60611,<br>Brookfield, US<div class="maps">Open in Maps</div></div>
    <div class="abs socials"><span style="background:#3b5998"></span><span style="background:#1da1f2"></span><span style="background:#c4302b"></span><span style="background:#cb2027"></span><span style="background:#dd4b39"></span></div>
    <div class="abs bottom">
      <div class="abs stats"><span>1,645 pets saved</span><span>9,227 donations</span><span>5,278 projects</span></div>
      <div class="abs copy">Copyright FurHaven 2013</div>
    </div>
  </footer>
</div>
</body>
</html>
```